Larkmont Business Card Design Project

Double side card , just the logo on oxford white background on one side , and the rest of the information on the other side..
the company name is : Larkmont International General Trading LLC.
logo is already attached
the card to show in the info side: company name, employee name and position (job title) phone number, fax number, email address, P.O. box, Location (city and country)
deadline is already extended 4 all to have more time... thanks

```html
<!DOCTYPE html>
<html lang="en">
<head>
<meta charset="utf-8">
<title>Larkmont Business Card</title>
<link href="https://fonts.googleapis.com/css2?family=Open+Sans:wght@400;600&display=swap" rel="stylesheet">
<style>
  :root {
    --backdrop: #d9dbde;
    --card: #ffffff;
    --card-back: #f4f5f6;
    --ink: #4a4d52;
    --ink-soft: #6b6e73;
    --accent: #2b8fd0;
    --accent-dark: #1f5f9c;
  }
  * { margin: 0; padding: 0; box-sizing: border-box; }
  html, body {
    width: 1200px; height: 900px; overflow: hidden;
    background: var(--backdrop);
    font-family: "Open Sans", Arial, sans-serif;
  }
  .sheet {
    width: 1200px; height: 900px;
    display: flex; flex-direction: column;
    align-items: center; justify-content: center; gap: 44px;
  }
  .card {
    position: relative;
    width: 630px; height: 360px;
    background: var(--card);
    box-shadow: 0 6px 18px rgba(0,0,0,0.18);
  }
  .card--logo {
    background: linear-gradient(160deg, #ffffff 0%, var(--card-back) 100%);
    display: flex; align-items: center; justify-content: center;
  }
  .wordmark {
    display: flex; align-items: center; gap: 14px;
    color: var(--ink);
    font-weight: 400;
    letter-spacing: 1px;
  }
  .wordmark__dot {
    width: 26px; height: 26px; border-radius: 50%;
    background: var(--accent);
  }
  .card--logo .wordmark { font-size: 42px; }

  .card--info .wordmark {
    position: absolute; left: 48px; top: 150px;
    font-size: 34px;
  }
  .card--info .wordmark__dot { width: 22px; height: 22px; }

  .person { position: absolute; left: 372px; top: 62px; }
  .person__name { font-size: 19px; font-weight: 600; color: var(--ink-soft); }
  .person__title { font-size: 14px; color: var(--accent); letter-spacing: 0.5px; margin-top: 1px; }

  .contact {
    position: absolute; left: 372px; top: 150px;
    font-size: 14px; line-height: 21px; color: var(--ink-soft);
  }
  .contact__phone { display: flex; align-items: center; gap: 8px; font-size: 16px; }
  .contact__icons { display: flex; gap: 4px; }
  .contact__address { margin-top: 10px; }

  .rule {
    position: absolute; height: 1.5px; background: var(--accent);
  }
  .rule--right { left: 372px; right: 0; top: 262px; }
  .rule--left { left: 0; width: 66px; bottom: 28px; }

  .website {
    position: absolute; left: 80px; bottom: 20px;
    font-size: 14px; letter-spacing: 2px; color: var(--ink-soft);
  }
</style>
</head>
<body>
<main class="sheet">
  <section class="card card--logo" aria-label="Card front">
    <div class="wordmark"><span class="wordmark__dot"></span><span>Larkmont Int.</span></div>
  </section>

  <section class="card card--info" aria-label="Card back">
    <div class="wordmark"><span class="wordmark__dot"></span><span>Larkmont Int.</span></div>

    <div class="person">
      <div class="person__name">Daniel Hartley</div>
      <div class="person__title">DIRECTOR</div>
    </div>

    <div class="contact">
      <div class="contact__phone">
        <span class="contact__icons">
          <svg width="13" height="13" viewBox="0 0 16 16" aria-label="Phone"><path fill="#2b8fd0" d="M3.5 1.5l2.5 3-1.5 1.8a9 9 0 0 0 5.2 5.2L11.5 10l3 2.5-1.5 2.5C7 15 1 9 1 3z"/></svg>
          <svg width="13" height="13" viewBox="0 0 16 16" aria-label="Fax"><rect x="4" y="1" width="8" height="5" fill="none" stroke="#2b8fd0" stroke-width="1.5"/><rect x="1" y="6" width="14" height="8" rx="1.5" fill="#2b8fd0"/><rect x="4" y="10" width="8" height="2" fill="#fff"/></svg>
        </span>
        <span>123.555.0198</span>
      </div>
      <div>dan@larkmont.com</div>
      <div class="contact__address">88 Harbor Lane - Suite 210<br>Coral Bay, SC 29500</div>
    </div>

    <div class="rule rule--right"></div>
    <div class="rule rule--left"></div>
    <div class="website">www.larkmont.com</div>
  </section>
</main>
</body>
</html>
```